Cat sitting business Web Design Project ***

I have a cat sitting business where I either take care of cats in their home or board them in mine

I need a website which offers my services, my rates, about me, FAQ's, Hours of operation and service areas covered, testimonials, contact info, newsletter sign up, gallery of photos and the ability for me to go in and update when needed.

Coding

Coded - Design and coding required

Number of Pages Required

5+ page

```html
<!DOCTYPE html>
<html lang="en">
<head>
<meta charset="utf-8">
<title>Velvet Paws Cat Care</title>
<link href="https://fonts.googleapis.com/css2?family=Nunito:ital,wght@0,400;0,600;0,700;1,400&family=Great+Vibes&display=swap" rel="stylesheet">
<style>
:root{
  --green:#8cc152;
  --green-dark:#7ab03f;
  --maroon:#a64d50;
  --grey-bg:#f1f1f1;
  --ink:#2b2b2b;
  --muted:#555;
  --white:#fff;
  --warm:#b9835a;
}
*{box-sizing:border-box;margin:0;padding:0}
html,body{width:1200px;height:4181px;overflow:hidden}
body{position:relative;font-family:"Nunito",sans-serif;color:var(--ink);background:var(--grey-bg)}
.abs{position:absolute}
.script{font-family:"Great Vibes",cursive;color:var(--maroon);font-weight:400}
.btn{position:absolute;display:flex;align-items:center;justify-content:center;border-radius:20px;color:var(--white);font-size:11px;font-weight:600}
.btn--maroon{background:var(--maroon)}
.btn--green{background:var(--green)}
.photo{position:absolute}

/* header */
.site-header{position:absolute;left:0;top:0;width:1200px;height:74px;background:var(--white);z-index:5}
.brand{position:absolute;left:100px;top:14px;display:flex;align-items:center;gap:8px}
.brand__dot{width:34px;height:34px;border-radius:50%;background:var(--green)}
.brand__name{font-size:14px;font-weight:700;color:var(--maroon);line-height:1.1;width:90px}
.nav a{position:absolute;top:28px;font-size:12.5px;color:var(--ink);text-decoration:none;font-weight:600}
.nav a.active{color:var(--green)}
.header-phone{position:absolute;left:866px;top:29px;font-size:12.5px;font-weight:700;display:flex;gap:6px;align-items:center}

/* hero */
.hero{position:absolute;left:0;top:74px;width:1200px;height:600px;overflow:hidden}
.hero__text{position:absolute;left:198px;top:122px;color:var(--white);z-index:2}
.hero__kicker{font-size:28px;font-weight:400}
.hero__kicker .script{color:var(--white);font-size:38px}
.hero__title{font-size:36px;font-weight:400;line-height:45px;margin-top:8px;width:620px}
.dots{position:absolute;left:988px;top:178px;display:flex;flex-direction:column;gap:10px;z-index:2}
.dots span{width:11px;height:11px;border:1.5px solid var(--white);border-radius:50%}
.dots span.on{background:var(--white)}

/* about */
.about-photo{left:200px;top:719px;width:362px;height:437px;background:linear-gradient(135deg,#e8d0a6,#8a6a4e 60%,#3a2c25)}
.about-bar{left:200px;top:719px;width:18px;height:410px;background:var(--green)}
.about-text{position:absolute;left:612px;top:748px;width:390px}
.about-text .script{font-size:30px}
.section-head{font-size:29px;color:var(--green);font-weight:400;line-height:36px;margin-top:8px}
.about-text p{font-size:10.5px;line-height:19px;color:var(--ink);margin-top:18px}
.signature{font-family:"Great Vibes",cursive;font-size:34px;color:var(--ink);margin-top:12px;margin-left:-14px}
.mini-logo{position:absolute;display:flex;align-items:center;gap:6px}
.mini-logo__dot{width:26px;height:26px;border-radius:50%;background:var(--green);opacity:.8}
.mini-logo__name{font-size:12px;font-weight:700;color:var(--maroon);width:70px;line-height:1.1}

.center-head{position:absolute;left:0;width:1200px;text-align:center}
.center-head .script{font-size:28px;display:block;line-height:30px}
.center-head h2{font-size:29px;color:var(--green);font-weight:400;line-height:36px}
.rule{position:absolute;left:200px;width:800px;height:2px}

/* services */
.service-card{position:absolute;top:1372px;width:182px;height:249px;color:var(--white)}
.service-card__label{position:absolute;left:0;right:0;bottom:18px;text-align:center;font-size:14px;font-weight:600}
.service-card--active{display:flex;flex-direction:column;align-items:center;justify-content:center;text-align:center;padding:0 10px}
.service-card--active h3{font-size:14px;font-weight:600;margin-top:50px}
.service-card--active p{font-size:9.5px;line-height:15px;margin-top:10px}
.service-card--active .circle{width:30px;height:30px;border:1.5px solid var(--white);border-radius:50%;margin-top:14px;display:flex;align-items:center;justify-content:center}

/* areas */
.areas{position:absolute;left:0;top:1747px;width:1200px;height:440px}
.areas__text{position:absolute;left:200px;top:50px;color:var(--white);z-index:2}
.areas__text .script{color:var(--white);font-size:30px;line-height:30px}
.areas__text h2{font-size:29px;font-weight:400;line-height:38px}
.area-list{display:grid;grid-template-columns:135px 130px;row-gap:3px;margin-top:12px;font-size:11px}
.area-list li{list-style:none;display:flex;align-items:center;gap:8px}

/* gallery */
.gallery-tile{position:absolute}

/* testimonial */
.quote{position:absolute;left:300px;top:3183px;width:600px;text-align:center;font-size:12.5px;font-style:italic;line-height:19px;color:var(--ink)}
.quote-author{position:absolute;left:0;width:1200px;top:3270px;text-align:center;font-size:11px;color:var(--green)}
.quote-author span{color:var(--maroon)}

/* quote form */
.quote-form{position:absolute;left:200px;top:3402px;width:362px;height:406px;background:var(--maroon);color:var(--white);z-index:3}
.quote-form h2{text-align:center;font-size:22px;font-weight:600;margin-top:42px}
.quote-form h2 .script{color:var(--white);font-size:28px}
.quote-form .sub{text-align:center;font-size:13px;margin-top:2px}
.field{position:absolute;background:var(--white);border-radius:3px;color:var(--ink);font-size:9.5px;padding:8px 18px}

/* footer */
.site-footer{position:absolute;left:0;top:3873px;width:1200px;height:308px;background:#f4f4f4}
.foot-col{position:absolute;top:60px;font-size:10px;line-height:15px;color:var(--ink)}
.foot-col h4{font-size:13px;color:var(--maroon);font-weight:600;margin-bottom:12px}
.foot-row{display:flex;gap:10px;align-items:center;margin-bottom:10px}
.social{position:absolute;top:4102px;width:30px;height:30px;border-radius:50%;background:var(--maroon)}
.social.alt{background:var(--green)}
</style>
</head>
<body>

<header class="site-header">
  <div class="brand"><span class="brand__dot"></span><span class="brand__name">Velvet Paws Cat Care</span></div>
  <nav class="nav">
    <a class="active" style="left:419px">Home</a>
    <a style="left:479px">About Me</a>
    <a style="left:562px">Services</a>
    <a style="left:638px">Price</a>
    <a style="left:693px">Gallery</a>
    <a style="left:762px">Testimonials</a>
  </nav>
  <div class="header-phone">
    <svg width="12" height="12" viewBox="0 0 24 24"><path fill="#8cc152" d="M6.6 10.8a15 15 0 0 0 6.6 6.6l2.2-2.2c.3-.3.7-.4 1-.2 1.1.4 2.3.6 3.6.6.6 0 1 .4 1 1V20c0 .6-.4 1-1 1A17 17 0 0 1 3 4c0-.6.4-1 1-1h3.5c.6 0 1 .4 1 1 0 1.3.2 2.5.6 3.6.1.3 0 .7-.2 1z"/></svg>
    555-201-3847
  </div>
  <div class="btn btn--maroon" style="left:1007px;top:22px;width:99px;height:30px">Contact Us</div>
</header>

<section class="hero">
  <div role="img" aria-label="Photo of a ginger cat sleeping on a cushion by a window" style="position:absolute;inset:0;background:linear-gradient(100deg,#8a8c8a 0%,#a09890 30%,#b98a5e 60%,#c47f45 80%,#8d6a4e 100%)"></div>
  <div style="position:absolute;inset:0;background:linear-gradient(90deg,rgba(0,0,0,.35),rgba(0,0,0,0) 60%)"></div>
  <svg class="abs" style="left:0;top:0" width="1200" height="600" viewBox="0 0 1200 600">
    <path d="M0 370 Q600 790 1200 410 L1200 600 L0 600 Z" fill="#f1f1f1"/>
    <path d="M60 420 Q600 820 1140 430" fill="none" stroke="#8cc152" stroke-width="5"/>
  </svg>
  <div class="hero__text">
    <div class="hero__kicker"><span class="script">Velvet Paws</span> Cat Care</div>
    <h1 class="hero__title">Lorem Ipsum is simply dummy text of the printing and typesetting industry.</h1>
  </div>
  <div class="btn btn--green" style="left:200px;top:329px;width:112px;height:32px;z-index:2">Contact Us</div>
  <div class="dots"><span></span><span class="on"></span><span></span><span></span></div>
</section>

<section class="about">
  <div class="mini-logo" style="left:1012px;top:646px"><span class="mini-logo__dot"></span><span class="mini-logo__name">Velvet Paws Cat Care</span></div>
  <div class="photo about-photo" role="img" aria-label="Photo of the cat sitter holding a white cat on a sofa"></div>
  <div class="photo about-bar"></div>
  <div class="about-text">
    <span class="script">About Me</span>
    <h2 class="section-head">Lorem Ipsum is simply dummy text the printing typesetting.</h2>
    <p>Lorem ipsum dolor sit amet, consectetur adipiscing elit, sed do eiusmod tempor incididunt ut labore et dolore magna aliqua. Lorem ipsum dolor sit amet, consectetur adipiscing elit, sed do eiusmod tempor incididunt ut labore et dolore magna aliqua. Lorem ipsum dolor sit amet, consectetur adipiscing elit, sed do eiusmod tempor incididunt ut labore et dolore magna aliqua.</p>
    <div class="signature">Marlene...</div>
  </div>
  <div class="btn btn--maroon" style="left:612px;top:1093px;width:114px;height:29px">Discover More</div>
  <div class="photo" role="img" aria-label="Photo of a ginger cat lying down" style="left:1020px;top:1133px;width:180px;height:114px;background:radial-gradient(ellipse at 60% 55%,#d08a45 0%,#c9843f 45%,rgba(241,241,241,0) 72%)"></div>
</section>

<div class="rule" style="top:1221px;background:var(--green);height:2px"></div>

<section class="services">
  <div class="center-head" style="top:1280px"><span class="script">What I Do</span><h2>My services</h2></div>
  <div class="service-card" role="img" aria-label="Photo of a cat sitting by a glass door" style="left:200px;background:linear-gradient(180deg,#c8ccc8,#9a8f80 60%,#4a4540)"><span class="service-card__label">Boarding</span></div>
  <div class="service-card service-card--active" style="left:406px;background:linear-gradient(180deg,#c9847a 0%,#b7957a 40%,#8cc152 100%)">
    <h3>House Sitting</h3>
    <p>Lorem Ipsum is simply dummy text of the printing and typesetting industry. Lorem Ipsum has been the industry's standard</p>
    <span class="circle"><svg width="12" height="12" viewBox="0 0 12 12"><path d="M2 6h8M7 3l3 3-3 3" stroke="#fff" stroke-width="1.4" fill="none"/></svg></span>
  </div>
  <div class="service-card" role="img" aria-label="Photo of a black and white cat walking outdoors" style="left:612px;background:linear-gradient(180deg,#7f8e82,#5c6a60 55%,#2f3530)"><span class="service-card__label">Cat Walking</span></div>
  <div class="service-card" role="img" aria-label="Photo of a woman holding a tabby cat" style="left:818px;background:linear-gradient(180deg,#e2ddd6,#b7a898 55%,#5d5048)"><span class="service-card__label">Cat Day Care</span></div>
  <div class="btn btn--maroon" style="left:531px;top:1653px;width:138px;height:31px">View All Services</div>
</section>

<section class="areas">
  <div role="img" aria-label="Photo of a tabby cat in a sunny garden with a small cat house" style="position:absolute;inset:0;background:linear-gradient(90deg,#8cc152 0%,#8cc152 38%,#a8c98a 55%,#c7d6b5 68%,#7e8e6c 82%,#5f6b58 100%)"></div>
  <svg class="abs" style="left:0;top:0" width="1200" height="440" viewBox="0 0 1200 440">
    <path d="M0 200 Q560 560 1200 260 L1200 440 L0 440 Z" fill="#f1f1f1"/>
    <path d="M100 280 Q600 600 1140 300" fill="none" stroke="#a64d50" stroke-width="5"/>
  </svg>
  <div class="areas__text">
    <span class="script">Area we Serve</span>
    <h2>Service areas covered</h2>
    <ul class="area-list">
      <li><svg width="10" height="8" viewBox="0 0 10 8"><path d="M1 4l3 3 5-6" stroke="#fff" stroke-width="1.6" fill="none"/></svg>Lorem ipsum</li>
      <li><svg width="10" height="8" viewBox="0 0 10 8"><path d="M1 4l3 3 5-6" stroke="#fff" stroke-width="1.6" fill="none"/></svg>Sed do eiusmod</li>
      <li><svg width="10" height="8" viewBox="0 0 10 8"><path d="M1 4l3 3 5-6" stroke="#fff" stroke-width="1.6" fill="none"/></svg>Dolor sit amet</li>
      <li><svg width="10" height="8" viewBox="0 0 10 8"><path d="M1 4l3 3 5-6" stroke="#fff" stroke-width="1.6" fill="none"/></svg>Adipiscing elit</li>
      <li><svg width="10" height="8" viewBox="0 0 10 8"><path d="M1 4l3 3 5-6" stroke="#fff" stroke-width="1.6" fill="none"/></svg>consectetur</li>
      <li><svg width="10" height="8" viewBox="0 0 10 8"><path d="M1 4l3 3 5-6" stroke="#fff" stroke-width="1.6" fill="none"/></svg>Sed do eiusmod</li>
      <li><svg width="10" height="8" viewBox="0 0 10 8"><path d="M1 4l3 3 5-6" stroke="#fff" stroke-width="1.6" fill="none"/></svg>Adipiscing elit</li>
      <li><svg width="10" height="8" viewBox="0 0 10 8"><path d="M1 4l3 3 5-6" stroke="#fff" stroke-width="1.6" fill="none"/></svg>Contrary popular</li>
      <li><svg width="10" height="8" viewBox="0 0 10 8"><path d="M1 4l3 3 5-6" stroke="#fff" stroke-width="1.6" fill="none"/></svg>Sed do eiusmod</li>
    </ul>
  </div>
  <div class="btn btn--maroon" style="left:200px;top:255px;width:100px;height:30px;z-index:2">Contact Us</div>
</section>

<section class="gallery">
  <div class="mini-logo" style="left:100px;top:2220px"><span class="mini-logo__dot"></span><span class="mini-logo__name">Velvet Paws Cat Care</span></div>
  <div class="center-head" style="top:2250px"><span class="script">Velvet Paws</span><h2>Photo Gallery</h2></div>
  <div class="gallery-tile" role="img" aria-label="Photo of a grey tabby cat" style="left:200px;top:2340px;width:250px;height:312px;background:linear-gradient(180deg,#e6e6e6,#9c9c98 55%,#6a6a66)"></div>
  <div class="gallery-tile" role="img" aria-label="Photo of a kitten among flowers and eggs" style="left:476px;top:2340px;width:250px;height:154px;background:linear-gradient(180deg,#e9e6e0,#c9b8a0 50%,#a6c49a)"></div>
  <div class="gallery-tile" role="img" aria-label="Photo of a woman hugging a ginger cat" style="left:750px;top:2340px;width:250px;height:312px;background:linear-gradient(180deg,#ece8e3,#b88e6c 45%,#6d87a8)"></div>
  <div class="gallery-tile" role="img" aria-label="Photo of a tabby cat sitting in a room" style="left:476px;top:2520px;width:250px;height:314px;background:linear-gradient(180deg,#f0eeea,#d8d2c8 50%,#8d7a66)"></div>
  <div class="gallery-tile" role="img" aria-label="Photo of a ginger cat resting on a blanket" style="left:200px;top:2678px;width:250px;height:156px;background:linear-gradient(180deg,#ecebe7,#d5d3cf 50%,#c58a52)"></div>
  <div class="gallery-tile" role="img" aria-label="Photo of a cat in a small wooden house" style="left:750px;top:2678px;width:250px;height:156px;background:linear-gradient(180deg,#f1efec,#c89a70 55%,#8a6248)"></div>
  <div class="btn btn--green" style="left:551px;top:2866px;width:99px;height:30px">View All</div>
  <div class="photo" role="img" aria-label="Photo of a ginger cat lying down" style="left:0;top:2871px;width:184px;height:109px;background:radial-gradient(ellipse at 50% 55%,#cf8645 0%,#c98040 45%,rgba(241,241,241,0) 72%)"></div>
  <div class="photo" role="img" aria-label="Photo of a ginger cat sitting" style="left:1056px;top:2826px;width:97px;height:130px;background:radial-gradient(ellipse at 50% 55%,#d89452 0%,#d08a48 45%,rgba(241,241,241,0) 72%)"></div>
</section>

<div class="rule" style="top:2957px;background:#555;height:1px"></div>

<section class="testimonials">
  <div class="center-head" style="top:3008px"><span class="script">Customer Review</span><h2>Happy clients say</h2></div>
  <div class="photo" role="img" aria-label="Portrait of a customer" style="left:564px;top:3095px;width:72px;height:72px;border-radius:50%;border:2px solid var(--maroon);background:radial-gradient(circle,#d9b9a0,#8a6a58)"></div>
  <svg class="abs" style="left:198px;top:3188px" width="16" height="24" viewBox="0 0 16 24"><path d="M13 2 3 12l10 10" stroke="#a64d50" stroke-width="1.6" fill="none"/></svg>
  <svg class="abs" style="left:986px;top:3188px" width="16" height="24" viewBox="0 0 16 24"><path d="M3 2l10 10L3 22" stroke="#a64d50" stroke-width="1.6" fill="none"/></svg>
  <p class="quote">"There are many variations of passages of Lorem Ipsum available, but the majority have suffered alteration in some form, by injected humour, or randomised words which don't look even slightly believable. If you are going to use a passage of lorem Ipsum, you need to be sure there isn't anything embarrassing."</p>
  <div class="quote-author">Standard Chunk <span>/ Loyal Customer</span></div>
  <div class="btn btn--maroon" style="left:551px;top:3313px;width:99px;height:28px">View All</div>
</section>

<section class="get-quote">
  <svg class="abs" style="left:0;top:3402px" width="1200" height="471" viewBox="0 0 1200 471" role="img" aria-label="Photo of a woman playing with a ginger cat">
    <defs>
      <linearGradient id="photoTone" x1="0" y1="0" x2="1" y2="0">
        <stop offset="0" stop-color="#a77a4e"/>
        <stop offset=".45" stop-color="#c4945f"/>
        <stop offset=".75" stop-color="#d9c8b8"/>
        <stop offset="1" stop-color="#8b8580"/>
      </linearGradient>
      <linearGradient id="leftTone" x1="0" y1="0" x2="1" y2="0">
        <stop offset="0" stop-color="#e4ecd8"/>
        <stop offset="1" stop-color="#f1f1f1"/>
      </linearGradient>
    </defs>
    <path d="M0 230 Q600 -90 1200 130 L1200 471 L0 471 Z" fill="url(#leftTone)"/>
    <path d="M560 70 Q880 -10 1200 130 L1200 471 L560 471 Z" fill="url(#photoTone)"/>
    <path d="M0 230 Q600 -90 1200 130" fill="none" stroke="#a64d50" stroke-width="4"/>
  </svg>
  <form class="quote-form">
    <h2>Get <span class="script">Free</span> Quote</h2>
    <p class="sub">Instantly Book Your Service Today!</p>
    <div class="field" style="left:26px;top:115px;width:150px;height:28px">Your Name</div>
    <div class="field" style="left:186px;top:115px;width:151px;height:28px">Phone</div>
    <div class="field" style="left:26px;top:159px;width:311px;height:28px">Email</div>
    <div class="field" style="left:26px;top:203px;width:311px;height:28px">Address</div>
    <div class="field" style="left:26px;top:245px;width:311px;height:72px">Type your Message ...</div>
    <div class="btn btn--green" style="left:138px;top:333px;width:86px;height:29px">Send</div>
  </form>
</section>

<footer class="site-footer">
  <div class="mini-logo" style="left:100px;top:108px"><span class="mini-logo__dot" style="width:34px;height:34px"></span><span class="mini-logo__name" style="font-size:14px;width:90px">Velvet Paws Cat Care</span></div>
  <div class="foot-col" style="left:291px">
    <h4>Contact Us</h4>
    <div class="foot-row" style="font-size:14px"><svg width="12" height="12" viewBox="0 0 24 24"><path fill="#8cc152" d="M6.6 10.8a15 15 0 0 0 6.6 6.6l2.2-2.2c.3-.3.7-.4 1-.2 1.1.4 2.3.6 3.6.6.6 0 1 .4 1 1V20c0 .6-.4 1-1 1A17 17 0 0 1 3 4c0-.6.4-1 1-1h3.5c.6 0 1 .4 1 1 0 1.3.2 2.5.6 3.6.1.3 0 .7-.2 1z"/></svg>555-201-3847</div>
    <div class="foot-row"><svg width="12" height="10" viewBox="0 0 24 20"><path fill="#8cc152" d="M2 2h20v16H2z"/><path d="M2 2l10 8 10-8" stroke="#fff" stroke-width="2" fill="none"/></svg>hello@velvetpawscatcare.com</div>
    <div class="foot-row" style="align-items:flex-start"><svg width="12" height="14" viewBox="0 0 24 28"><path fill="#8cc152" d="M12 0a9 9 0 0 0-9 9c0 7 9 19 9 19s9-12 9-19a9 9 0 0 0-9-9zm0 12a3 3 0 1 1 0-6 3 3 0 0 1 0 6z"/></svg><span>12 Example Lane, Brookfield,<br>ON A1B 2C3</span></div>
  </div>
  <div class="foot-col" style="left:534px">
    <h4>Quick Links</h4>
    Home<br>About Me<br>Services<br>Price<br>Gallery<br>Testimonials<br>FAQ's<br>Contact Us
  </div>
  <div class="foot-col" style="left:664px">
    <h4>Working Hours</h4>
    Mon. to Fri. - 9:00am-7:00pm<br><span style="line-height:22px">Saturday - 10:00am-6:00pm</span><br>Sunday - Closed
  </div>
  <div class="foot-col" style="left:856px">
    <h4>Subscribe Us</h4>
  </div>
  <div class="abs" style="left:856px;top:93px;width:250px;height:29px;border:1.5px solid var(--maroon);border-radius:15px;background:#fff;font-size:10px;padding:7px 14px">name@email.com</div>
  <div class="btn btn--green" style="left:856px;top:138px;width:99px;height:29px">Subscribe</div>
  <div class="abs" style="left:93px;top:238px;font-size:10px">© 2022 Velvet Paws Cat Care. All Right Reserved</div>
  <svg class="abs" style="left:1144px;top:236px" width="18" height="18" viewBox="0 0 18 18"><path d="M9 1 17 17 9 12 1 17z" fill="#a64d50"/></svg>
</footer>
<span class="social" style="left:857px" aria-label="Social link"></span>
<span class="social alt" style="left:894px" aria-label="Social link"></span>
<span class="social" style="left:932px" aria-label="Social link"></span>
<span class="social" style="left:969px" aria-label="Social link"></span>

</body>
</html>
```